Roll-up-Banner für Schule gesucht
Zielgruppe
Unsere Schule wünscht einen Rollup (880mm Breite x 2200mm Höhe) für die jährliche Lesenacht für Kinder im Alter von 6-12 Jahren. Diese wären die Produktdaten: https://blaetter.vimtral-laden.de/ro-04-85-roll-up-display-basic-85-produktblatt-productsheet.pdf
Der Rollup sollte für Kinder kreiert werden aber nicht zu kindlich sein.
Aufgabenstellung
Das Logo der Schule müsste ersichtlich sein ansonsten ist Kreativität gefragt ;-)

```html
<!DOCTYPE html>
<html lang="de">
<head>
<meta charset="utf-8">
<title>Roll-up Lesenacht – Schule Birkenau</title>
<link rel="stylesheet" href="https://fonts.googleapis.com/css2?family=Source+Sans+3:wght@600;700&family=Satisfy&display=swap">
<style>
  :root {
    --stage: #43464b;
    --banner-top: #dadada;
    --banner-mid: #8c8c8c;
    --banner-deep: #474747;
    --quote-panel: rgba(235, 235, 235, 0.55);
    --ink-light: #f4f4f4;
    --logo-ink: #2e2e2e;
    --photo-warm: #b08a5c;
    --photo-glow: #e9c36a;
    --photo-shade: #5a5648;
  }
  * { margin: 0; padding: 0; box-sizing: border-box; }
  html, body {
    width: 768px; height: 1200px; overflow: hidden;
    background: var(--stage);
  }
  .rollup {
    position: absolute; left: 126px; top: 0;
    width: 516px; height: 1200px; overflow: hidden;
    background: linear-gradient(180deg,
      var(--banner-top) 0%, #b9b9b9 28%, var(--banner-mid) 48%,
      #5e5e5e 62%, var(--banner-deep) 72%, var(--banner-deep) 100%);
    font-family: "Source Sans 3", Arial, sans-serif;
  }
  .school-name {
    position: absolute; top: 140px; left: 0; width: 100%;
    text-align: center;
    font-weight: 700; font-size: 30px; letter-spacing: 6px;
    text-transform: uppercase; color: var(--logo-ink);
  }
  .quote-shapes { position: absolute; left: 0; top: 0; }
  .quote-text {
    position: absolute; left: 60px; top: 320px; width: 430px;
    text-align: center;
    font-family: "Satisfy", cursive;
    font-size: 34px; line-height: 62px;
    color: var(--ink-light);
  }
  .quote-mark {
    position: absolute; left: 412px; top: 548px;
    font-family: Georgia, serif; font-weight: 700;
    font-size: 130px; line-height: 1; color: var(--ink-light);
  }
  .quote-author {
    position: absolute; right: 36px; top: 656px;
    font-weight: 600; font-size: 17px; letter-spacing: 0.4px;
    color: var(--ink-light);
  }
  .reading-photo {
    position: absolute; left: 0; top: 760px; width: 100%; height: 440px;
    background:
      radial-gradient(circle at 88% 78%, var(--photo-glow) 0%, rgba(233,195,106,0) 30%),
      radial-gradient(ellipse at 25% 55%, #c9a07c 0%, rgba(201,160,124,0) 45%),
      linear-gradient(180deg, rgba(71,71,71,1) 0%, var(--photo-shade) 22%, var(--photo-warm) 70%, #7a6448 100%);
  }
</style>
</head>
<body>
  <main class="rollup">
    <div class="school-name">Schule Birkenau</div>

    <svg class="quote-shapes" width="516" height="700" viewBox="0 0 516 700" aria-hidden="true">
      <polygon class="quote-panel" points="72,265 519,331 519,604 72,576" fill="var(--quote-panel)"/>
      <polygon class="speech-bubble" points="38,305 480,260 480,641 163,621 104,662 122,619 52,615"
               fill="none" stroke="var(--ink-light)" stroke-width="1.6" stroke-linejoin="miter"/>
    </svg>

    <p class="quote-text">Von allen Welten, die der<br>Mensch erschaffen hat,<br>ist die der Bücher die<br>Gewaltigste.</p>
    <div class="quote-mark">”</div>
    <div class="quote-author">Heinrich Haldner</div>

    <div class="reading-photo" role="img" aria-label="Foto: Kind liest abends unter einer Decke ein Buch im warmen Licht einer Laterne"></div>
  </main>
</body>
</html>
```